Chiropractic healthcare group business card

We are a Portland Oregon based chiropractic healthcare group. Looking for a new business card design. Something cutting edge, that shows off our new logo and tag line.Use either of the attached logos.Our tag line = "Move freely. Live fully."I'm open to about anything, impress me!!
Target Market(s)
Chiropractic patients - Auto injury, back pain, sports injuries, neck , shoulder, hip, knee, ankle pain.
Industry/Entity Type
Chiropractic
Contact Information for Business Card
Dr. Bram Holtvick, D.C.
Clinic name - Fernway Chiropractic
2 clinics
location #1
20418 NW Marwick Road
Suite 4
Alder Falls, OR 97990
Location #2
13529 SE Calloway Street
Cedar Bluff, OR 97991
Main phone line 971.555.0143
website : www.FernwayClinics.example
Tag line "Move freely. Live fully."
Colors
Designer to choose colors to be used in the design.
Requirements
Must have
- Use the logo colors -- Want the orange color to be a TRUE orange.
- Both clinic address
- phone number
- website
- personal email - b.holtvick@ReliefBeginsHere.example
- tag line - "Move freely. Live fully."

```html
<!DOCTYPE html>
<html lang="en">
<head>
<meta charset="utf-8">
<title>Fernway Chiropractic – Business Card</title>
<link rel="stylesheet" href="https://fonts.googleapis.com/css2?family=Open+Sans:wght@400;600;700&display=swap">
<style>
  :root {
    --orange: #f7941d;
    --black: #141414;
    --black-soft: #262626;
    --white: #ffffff;
    --paper: #f6f4f2;
    --grey: #8a8a8a;
    --ink: #1b1b1b;
    --stage: #d9d5cf;
  }
  * { box-sizing: border-box; margin: 0; padding: 0; }
  html, body { width: 1200px; height: 942px; overflow: hidden; }
  body {
    background: var(--stage);
    font-family: "Open Sans", sans-serif;
    position: relative;
  }
  .card {
    position: absolute;
    top: 86px;
    width: 440px;
    height: 770px;
    overflow: hidden;
    box-shadow: 0 10px 30px rgba(0,0,0,.25);
  }
  .card--front { left: 130px; background: linear-gradient(160deg, var(--black-soft), var(--black) 60%); }
  .card--back  { left: 630px; background: linear-gradient(160deg, #2c2c2c 0%, var(--black) 55%, #1d1d1d 100%); }

  /* front */
  .front-head {
    position: absolute; left: 0; top: 0; width: 100%; height: 300px;
    background: linear-gradient(160deg, var(--white), var(--paper));
    border-bottom: 5px solid var(--orange);
    display: flex; align-items: center; justify-content: center;
  }
  .brand { display: flex; align-items: center; gap: 14px; }
  .brand__mark { width: 22px; height: 22px; background: var(--orange); }
  .brand__name {
    font-weight: 700; letter-spacing: 5px; text-transform: uppercase;
    line-height: 1.25; font-size: 26px; color: var(--ink);
  }
  .brand__name span { display: block; font-size: 15px; letter-spacing: 4px; }

  .contact-list { position: absolute; left: 0; top: 305px; width: 100%; list-style: none; }
  .contact-row {
    height: 72px; display: flex; align-items: center; gap: 20px;
    padding-left: 28px; padding-right: 18px;
    border-bottom: 1.5px solid var(--orange);
    color: var(--white); font-size: 17px;
  }
  .contact-row--name { height: 88px; font-size: 19px; line-height: 1.2; text-transform: uppercase; }
  .contact-row--email { font-size: 15.5px; }
  .icon { width: 42px; height: 42px; flex: none; }

  .addresses {
    position: absolute; left: 0; top: 609px; width: 100%; height: 161px;
    display: flex; align-items: flex-end; padding: 0 18px 22px 28px; gap: 16px;
  }
  .addresses__text {
    border-left: 2px solid var(--orange); padding-left: 16px;
    color: var(--white); font-size: 16.5px; line-height: 1.25;
  }
  .addresses__text p + p { margin-top: 10px; }

  /* back */
  .back-brand {
    position: absolute; left: 0; top: 250px; width: 100%;
    display: flex; justify-content: center;
  }
  .card--back .brand__name { color: var(--grey); }
  .tagline {
    position: absolute; left: 30px; right: 30px; top: 600px; height: 80px;
    border-top: 2px solid var(--orange); border-bottom: 2px solid var(--orange);
    display: flex; align-items: center; justify-content: center;
    color: var(--white); font-size: 25px; white-space: nowrap;
  }
</style>
</head>
<body>

<section class="card card--front" aria-label="Business card front">
  <header class="front-head">
    <div class="brand">
      <div class="brand__mark"></div>
      <div class="brand__name">Fernway<span>Chiropractic</span></div>
    </div>
  </header>

  <ul class="contact-list">
    <li class="contact-row contact-row--name">
      <svg class="icon" viewBox="0 0 42 42" aria-hidden="true">
        <circle cx="21" cy="21" r="19" fill="none" stroke="#fff" stroke-width="2.5"/>
        <circle cx="21" cy="16" r="6" fill="#fff"/>
        <path d="M10 32c2-7 20-7 22 0z" fill="#fff"/>
      </svg>
      <span>Dr. Bram Holtvick,<br>D.C.</span>
    </li>
    <li class="contact-row">
      <svg class="icon" viewBox="0 0 42 42" aria-hidden="true">
        <circle cx="21" cy="21" r="19" fill="none" stroke="#fff" stroke-width="2.5"/>
        <path d="M14 12c-2 2-2 6 2 11s9 8 12 7l2-3-4-3-2 2c-2-1-5-4-6-6l2-2-3-4z" fill="#fff"/>
      </svg>
      <span>971.555.0143</span>
    </li>
    <li class="contact-row">
      <svg class="icon" viewBox="0 0 42 42" aria-hidden="true">
        <g fill="none" stroke="#fff" stroke-width="2.2">
          <circle cx="21" cy="21" r="17"/>
          <ellipse cx="21" cy="21" rx="7" ry="17"/>
          <path d="M4 21h34M7 13h28M7 29h28"/>
        </g>
      </svg>
      <span>www.FernwayClinics.example</span>
    </li>
    <li class="contact-row contact-row--email">
      <svg class="icon" viewBox="0 0 42 42" aria-hidden="true">
        <rect x="5" y="10" width="32" height="22" fill="none" stroke="#fff" stroke-width="2.5"/>
        <path d="M5 10l16 13 16-13" fill="none" stroke="#fff" stroke-width="2.5"/>
      </svg>
      <span>b.holtvick@ReliefBeginsHere.example</span>
    </li>
  </ul>

  <div class="addresses">
    <svg class="icon" viewBox="0 0 42 42" aria-hidden="true">
      <path d="M5 20L21 6l16 14v16H5z" fill="none" stroke="#fff" stroke-width="2.5"/>
      <path d="M21 33c-5-6-7-9-7-12a7 7 0 0 1 14 0c0 3-2 6-7 12z" fill="#fff"/>
      <circle cx="21" cy="21" r="2.6" fill="#141414"/>
    </svg>
    <div class="addresses__text">
      <p>20418 NW Marwick Road Suite 4<br>Alder Falls, OR 97990</p>
      <p>13529 SE Calloway Street<br>Cedar Bluff, OR 97991</p>
    </div>
  </div>
</section>

<section class="card card--back" aria-label="Business card back">
  <div class="back-brand">
    <div class="brand">
      <div class="brand__mark"></div>
      <div class="brand__name">Fernway<span>Chiropractic</span></div>
    </div>
  </div>
  <p class="tagline">Move freely. Live fully.</p>
</section>

</body>
</html>
```